Technological Event Invitation

We need a invitation design for a technological event we are hosting along with our partner. The target of this event are Vice president, Managers and CEO of the most important companies (bank, insurrance companies, other) in the dominican republic.

It is a flat invitation and the size is 5” x 7”.

Title: API Management
"Transforma tu negocio con API Management a través de la estrategia de digitalización"
Date: Jueves 10 de Marzo del 2016
Time: 9:00 am - 5 pm.
Place: Resturant Casa Rivolta C/ Marcos Ibarra Lugo esq. Tomás Revel.
Host: Novaldo, SRL & KV Systems
RSVP: 809 555 47 13

The final design should have two logo one being Novaldo ( the company hosting the event) and KV logo ( partner). Please consider that the desgin should represent tecnhology world.

Target Market(s)

Financial Institutions,Corporations, Goverment Institution

Industry/Entity Type

Event

Requirements
Must have
• 1. Kv logo
• 2. novaldo Logo
• 3. The invitation should show that the is a tecnological event on APIM.
Nice to have
• our colors integrated on the invitations

```html
<!DOCTYPE html>
<html lang="es">
<head>
<meta charset="utf-8">
<title>API Management — Invitación</title>
<link href="https://fonts.googleapis.com/css2?family=Exo+2:wght@400;500;700;800;900&display=swap" rel="stylesheet">
<style>
  :root {
    --page-bg: #e8e8e8;
    --paper: #ffffff;
    --sky-blue: #5286c8;
    --red-top: #d84535;
    --red-bottom: #ae2830;
    --ink: #2b2b2b;
    --white: #ffffff;
    --partner-blue: #3f7cc4;
  }
  * { margin: 0; padding: 0; box-sizing: border-box; }
  html, body {
    width: 1200px; height: 1200px; overflow: hidden;
    background: var(--page-bg);
    font-family: "Exo 2", sans-serif;
  }
  .invitation {
    position: absolute; left: 192px; top: 65px;
    width: 816px; height: 1069px;
    background: var(--paper);
    overflow: hidden;
  }
  .band-blue {
    position: absolute; left: 0; top: 0; width: 100%; height: 383px;
    background: var(--sky-blue);
  }
  .band-red {
    position: absolute; left: 0; top: 383px; width: 100%; height: 337px;
    background: linear-gradient(180deg, var(--red-top), var(--red-bottom));
  }
  .hero-art {
    position: absolute; left: -150px; top: 200px;
    width: 440px; height: 440px; border-radius: 50%;
    background: radial-gradient(circle at 55% 40%, #f4f4f4 0%, #d9d9d9 55%, #a9a9a9 100%);
  }
  .title {
    position: absolute; right: 28px; color: var(--white);
    line-height: 1; text-align: right; white-space: nowrap;
  }
  .title-top { top: 158px; font-size: 96px; font-weight: 800; letter-spacing: -1px; }
  .title-main { top: 262px; font-size: 100px; font-weight: 900; letter-spacing: -2px; }
  .tagline {
    position: absolute; left: 400px; top: 402px; width: 390px;
    color: var(--white); font-size: 20px; font-weight: 500; line-height: 26px;
  }
  .details {
    position: absolute; left: 0; top: 512px;
    color: var(--white); font-size: 20px; font-weight: 400; line-height: 1;
  }
  .detail-row { position: relative; height: 32px; }
  .detail-row.wrap { height: 27px; }
  .detail-row.gap { margin-top: 8px; }
  .detail-label { position: absolute; left: 270px; width: 115px; text-align: right; }
  .detail-value { position: absolute; left: 400px; white-space: nowrap; }
  .sponsors {
    position: absolute; left: 0; top: 900px; width: 100%; height: 100px;
  }
  .host {
    position: absolute; left: 235px; top: 4px;
    display: flex; align-items: center; gap: 14px;
  }
  .host-mark {
    width: 72px; height: 72px; border-radius: 50%;
    background: var(--red-top);
  }
  .host-name {
    font-size: 50px; font-weight: 700; color: var(--ink);
    line-height: 1; letter-spacing: 1px;
  }
  .host-tagline {
    font-size: 16px; font-weight: 500; color: var(--ink);
    letter-spacing: 1px; margin-top: 6px;
  }
  .partner {
    position: absolute; left: 670px; top: 0;
    font-size: 84px; font-weight: 800; color: var(--partner-blue);
    line-height: 1;
  }
</style>
</head>
<body>
  <main class="invitation">
    <div class="band-blue"></div>
    <div class="band-red"></div>

    <div class="hero-art" role="img" aria-label="Esfera formada por teclas de teclado blancas con una franja de teclas rojas"></div>

    <h1>
      <span class="title title-top">API</span>
      <span class="title title-main">MANAGEMENT</span>
    </h1>

    <p class="tagline">“Transforma tu negocio con API Management a través de la estrategia de digitalización”</p>

    <section class="details">
      <div class="detail-row"><span class="detail-label">Fecha:</span><span class="detail-value">Jueves 10 de Marzo del 2016</span></div>
      <div class="detail-row"><span class="detail-label">Hora:</span><span class="detail-value">9:00 a.m. &nbsp;-&nbsp; 5:00 p.m.</span></div>
      <div class="detail-row wrap"><span class="detail-label">Lugar:</span><span class="detail-value">Resturant Casa Rivolta,</span></div>
      <div class="detail-row wrap"><span class="detail-value">C/ Marcos Ibarra Lugo esq. Tomás Revel.</span></div>
      <div class="detail-row gap"><span class="detail-label">RSVP:</span><span class="detail-value">809 555 47 13</span></div>
    </section>

    <footer class="sponsors">
      <div class="host">
        <span class="host-mark" aria-hidden="true"></span>
        <div>
          <div class="host-name">NOVALDO</div>
          <div class="host-tagline">IT CONSULTING AND SERVICES</div>
        </div>
      </div>
      <div class="partner">KV</div>
    </footer>
  </main>
</body>
</html>
```